Carewell Hub Needs a Web Design

Designers will use (and improve) our mockups to re-design our mobile-friendly website. We would like to see designs that use the color blue (as our logo in the attached file). The final design should convey convenience and communicate accessible health and wellness.

We need a web design for a company based in Kampala called 'Carewell Hub'.

We help patients to compare health insurance, find a doctor and book an appointment instantly.

Our initial products are Find and Book - a Wordpress database that helps patients to find a doctor and book an appointment instantly; and Insurance - a database that helps patients compare health insurance policies online. We would like to see designs that are mobile-friendly and responsive with awesome user interface and experience.
Updates

Project Deadline Extended Reason: We need web design of 5+ pages. Please see attached files for guidance. Added Wednesday, February 17, 2016

Industry/Entity Type

Health Service

Number of Pages Required

5+ page

Font styles to use
Sans Serif

Colors
33a6d7
85cae6
cee9f5
ecf7fb

Requirements
Must have
• Mobile-friendly and responsive design with awesome UI and UX

```html
<!DOCTYPE html>
<html lang="en">
<head>
<meta charset="utf-8">
<title>Carewell Hub — Home</title>
<link href="https://fonts.googleapis.com/css2?family=Raleway:ital,wght@0,300;0,400;0,600;0,700;1,400&family=Montserrat:wght@400;600;700&display=swap" rel="stylesheet">
<style>
:root{
  --nav:#62abe2;
  --hero:#ebf6fb;
  --blue:#33a6d7;
  --blue-deep:#3b8fe0;
  --blue-bright:#4fb3ec;
  --title:#3a9ad9;
  --green:#3fd4a8;
  --green-2:#48cbb8;
  --red:#e5484d;
  --ink:#3b4149;
  --muted:#9aa3ab;
  --line:#e6eaee;
  --card:#f0f0f0;
  --stat-bg:#ededed;
  --footer:#4a9fe0;
  --white:#ffffff;
}
*{box-sizing:border-box;margin:0;padding:0}
html,body{width:1200px;height:1200px;overflow:hidden;background:var(--white)}
body{font-family:'Raleway',sans-serif;color:var(--ink)}
.stage{position:absolute;left:0;top:0;width:1500px;height:1500px;transform:scale(.8);transform-origin:0 0}
.abs{position:absolute}
.center{text-align:center}
/* nav */
.nav{left:475px;top:2px;width:551px;height:26px;background:var(--nav)}
.brand{left:583px;top:8px;color:var(--white);font-size:10.5px;font-weight:400;display:flex;align-items:center;gap:4px}
.brand i{display:inline-block;width:8px;height:8px;border:1.2px solid var(--white);border-radius:50%}
.menu{left:697px;top:12px;display:flex;gap:9px;font-family:'Montserrat',sans-serif;font-size:4.2px;color:#dbeefb;letter-spacing:.2px}
.menu b{color:var(--white);font-weight:700}
.btn-appt{left:871px;top:8px;width:47px;height:13px;border-radius:7px;background:var(--green);color:var(--white);font:700 3.8px 'Montserrat',sans-serif;display:flex;align-items:center;justify-content:center}
/* hero */
.hero{left:475px;top:28px;width:551px;height:261px;background:var(--hero)}
.hero-title{left:582px;top:91px;color:var(--title);font-size:14px;line-height:19px;font-weight:400}
.hero-sub{left:582px;top:153px;font-size:4.4px;color:var(--title)}
.btn-outline{border:1px solid var(--title);border-radius:10px;color:var(--title);font:600 4.4px 'Montserrat',sans-serif;display:flex;align-items:center;justify-content:center}
.arrow{width:19px;height:19px;border-radius:50%;background:#dbeef9;color:var(--title);font-size:8px;display:flex;align-items:center;justify-content:center}
/* cta */
.cta{left:583px;width:335px;height:36px;background:linear-gradient(90deg,#45d6b0,#3ccf9f);color:var(--white)}
.cta-text{left:13px;top:8px;font-size:8px;line-height:11px;letter-spacing:.3px}
.btn-light{border:1px solid var(--white);border-radius:10px;color:var(--white);font:600 4.4px 'Montserrat',sans-serif;display:flex;align-items:center;justify-content:center}
/* intro */
.intro-title{left:583px;top:325px;width:335px;font-size:8.6px;line-height:12px;color:var(--ink);font-weight:600}
.tiny{font-size:4px;line-height:12px;color:var(--muted)}
.divider{height:1px;background:#ccd3d8}
.feature{width:110px;text-align:center}
.feature h4{font:700 3.8px 'Montserrat',sans-serif;margin-top:4px}
.feature p{font-size:3.6px;color:var(--muted);margin-top:3px}
/* departments */
.depts{left:475px;top:460px;width:551px;height:231px;background:linear-gradient(180deg,#3b8fe0,#4eb0ec)}
.sec-title-w{color:var(--white);font-size:10px;font-weight:300}
.dept{width:60px;text-align:center}
.dept .ring{width:44px;height:44px;margin:0 auto;border-radius:50%;background:var(--white);border:2px solid #cfe6f8;display:flex;align-items:center;justify-content:center}
.dept span{display:block;margin-top:9px;font:700 3.6px 'Montserrat',sans-serif;color:var(--white)}
/* doctors */
.sec-title{color:var(--ink);font-size:10px;font-weight:400}
.doc{width:77px;height:97px;background:var(--white);border:1px solid var(--line)}
.doc .photo{height:76px;background:var(--card)}
.doc .social{position:absolute;left:0;top:60px;width:77px;height:16px;background:var(--blue-deep);display:flex;justify-content:center;align-items:center;gap:3px}
.doc .social i{width:10px;height:10px;border-radius:50%;border:1px solid var(--white)}
.doc h5{font:700 3.8px 'Montserrat',sans-serif;text-align:center;margin-top:7px}
.doc p{font-size:3.6px;text-align:center;color:var(--green)}
/* testimonial */
.testi{left:475px;top:888px;width:551px;height:164px;background:linear-gradient(100deg,#48cbb8 30%,#4a9fdf)}
.avatar{left:722px;top:930px;width:57px;height:57px;border-radius:50%;background:radial-gradient(circle at 50% 40%,#e7b47f,#c4713f 60%,#4a6fb8);border:2px solid rgba(255,255,255,.6)}
.quote{left:600px;top:1009px;width:300px;font-size:4.8px;line-height:7px;font-style:italic;color:var(--white);text-align:center}
/* news */
.news{width:163px;height:58px;background:var(--white);border:1px solid var(--line)}
.news .thumb{position:absolute;left:0;top:0;width:57px;height:56px;background:var(--card)}
.news .date{position:absolute;left:0;top:0;width:14px;height:12px;background:var(--green);color:var(--white);font:700 4px/6px 'Montserrat',sans-serif;text-align:center;padding-top:1px}
.news .body{position:absolute;left:63px;top:5px;width:95px}
.news h6{font:700 4px/5px 'Montserrat',sans-serif}
.news p{font-size:3.3px;line-height:4.6px;color:var(--muted);margin-top:2px}
.news .meta{display:flex;justify-content:space-between;font-size:3.3px;color:var(--ink);margin-top:3px}
.news .meta em{color:var(--red);font-style:normal}
/* stats */
.stats{left:475px;top:1251px;width:551px;height:96px;background:var(--stat-bg)}
.map{left:520px;top:1255px;width:460px;height:90px;background:radial-gradient(ellipse at center,#e2e2e2,#ededed 70%)}
.stat{width:120px;text-align:center}
.stat b{display:block;font:700 15px 'Montserrat',sans-serif;color:var(--red)}
.stat span{display:block;font-size:9px;color:var(--ink)}
.stat i{display:block;width:20px;height:1px;background:#c7ccd1;margin:4px auto}
.stat p{font-size:3.6px;line-height:5px;color:var(--muted)}
/* footer */
.footer{left:475px;top:1347px;width:551px;height:136px;background:var(--footer)}
.fcol{width:105px;color:var(--white)}
.fcol h6{font:700 4.4px 'Montserrat',sans-serif;letter-spacing:.3px}
.fcol p{font-size:3.4px;line-height:5px;color:#e2f0fc;margin-top:4px}
.social-row{display:flex;gap:3px}
.social-row i{width:11px;height:11px;border-radius:50%;border:1px solid var(--white)}
.copy{left:475px;top:1488px;width:551px;font:700 3.4px 'Montserrat',sans-serif;color:var(--ink);text-align:center}
</style>
</head>
<body>
<div class="stage">

  <!-- navigation -->
  <div class="abs nav"></div>
  <div class="abs brand"><i></i>Carewell Hub</div>
  <div class="abs menu"><b>HOME</b><span>SERVICES</span><span>DOCTORS</span><span>NEWS</span><span>TIMETABLE</span><span>CONTACTS</span></div>
  <div class="abs btn-appt">APPOINTMENT</div>

  <!-- hero -->
  <div class="abs hero"></div>
  <div class="abs hero-title">MEDICAL REPORT<br>analysis acurately<br>structured.</div>
  <div class="abs hero-sub">Health have derived the fastest means to  acess medical report</div>
  <div class="abs btn-outline" style="left:583px;top:182px;width:68px;height:19px">LEARN MORE +</div>
  <div class="abs arrow" style="left:540px;top:141px">&#8592;</div>
  <div class="abs arrow" style="left:942px;top:141px">&#8594;</div>

  <!-- appointment call -->
  <div class="abs cta" style="top:271px">
    <div class="abs cta-text">IF YOU NEED A DOCTOR?<br><b style="font-family:Montserrat,sans-serif;font-size:7.5px">MAKE AN APPOINTMENT NOW !</b></div>
    <div class="abs btn-light" style="left:241px;top:8px;width:80px;height:19px">GET AN APPOINTMENT</div>
  </div>

  <!-- services intro -->
  <div class="abs intro-title center">Our Services are international certified which enables<br>us to accomodate international paitents</div>
  <div class="abs tiny center" style="left:583px;top:350px;width:335px">Aenean sollicitudin, lorem quis bibendum auctor, nisi elit consequat ipsum, nec sagittis sem nibh id elit. Duis sed odio sit amet<br>nibh vulputate cursus a sit amet mauris. Morbi accumsan ipsum velit. Nam nec tellus a odio tincidun</div>
  <div class="abs divider" style="left:740px;top:379px;width:20px"></div>

  <div class="abs feature" style="left:580px;top:393px">
    <svg width="26" height="26" viewBox="0 0 26 26"><rect x="2" y="6" width="22" height="18" rx="2" fill="#1e6fd9"/><rect x="9" y="2" width="8" height="5" rx="1" fill="none" stroke="#1e6fd9" stroke-width="2"/><path d="M11 10h4v4h4v4h-4v4h-4v-4H7v-4h4z" fill="#fff"/></svg>
    <h4 style="color:var(--green)">ADVANCED TECHNOLOGY</h4><p>Ipsum dolor sit amet consectetur adipiscing</p>
  </div>
  <div class="abs feature" style="left:695px;top:393px">
    <svg width="30" height="26" viewBox="0 0 30 26"><path d="M15 24C6 17 2 12 2 8a6 6 0 0 1 13-2 6 6 0 0 1 13 2c0 4-4 9-13 16z" fill="none" stroke="#e5484d" stroke-width="2"/><path d="M5 13h6l2-4 3 8 2-4h7" fill="none" stroke="#e5484d" stroke-width="1.6"/></svg>
    <h4>HEALTHCARE SOLUTION</h4><p>Lorem ipsum dolor sit amet consectetur</p>
  </div>
  <div class="abs feature" style="left:810px;top:393px">
    <svg width="30" height="26" viewBox="0 0 30 26"><path d="M2 6h16v14H2zM18 10h6l4 5v5H18z" fill="#e5484d"/><circle cx="8" cy="21" r="3" fill="#fff" stroke="#e5484d" stroke-width="1.5"/><circle cx="22" cy="21" r="3" fill="#fff" stroke="#e5484d" stroke-width="1.5"/><path d="M8 9h3v3h3v3h-3v3H8v-3H5v-3h3z" fill="#fff"/></svg>
    <h4>SERVICE 24/7</h4><p>Call +1 800 555 0123 for emergency</p>
  </div>

  <!-- departments -->
  <div class="abs depts"></div>
  <div class="abs sec-title-w center" style="left:475px;top:472px;width:551px">What we do</div>
  <div class="abs" style="left:740px;top:487px;width:20px;height:1px;background:#9fd0f4"></div>

  <div class="abs dept" style="left:591px;top:500px"><div class="ring"><svg width="18" height="20" viewBox="0 0 18 20"><path d="M3 2c3-1 4 1 6 1s3-2 6-1c3 2 2 7 0 10-1 3-1 7-3 7s-1-6-3-6-1 6-3 6-2-4-3-7C1 9 0 4 3 2z" fill="none" stroke="#3b8fe0" stroke-width="1.6"/></svg></div><span>DENTAL</span></div>
  <div class="abs dept" style="left:677px;top:500px"><div class="ring"><svg width="22" height="14" viewBox="0 0 22 14"><path d="M1 7h6l2-5 3 10 2-5h7" fill="none" stroke="#3b8fe0" stroke-width="1.6"/></svg></div><span>CARDIOLOGY</span></div>
  <div class="abs dept" style="left:763px;top:500px"><div class="ring"><svg width="20" height="18" viewBox="0 0 20 18"><path d="M3 10C0 8 2 3 6 3c1-2 6-3 8 0 4 0 6 4 4 7-1 2-4 2-6 2l-1 4h-3l1-4C6 12 4 12 3 10z" fill="#3b8fe0"/></svg></div><span>NEUROLOGY</span></div>
  <div class="abs dept" style="left:849px;top:500px"><div class="ring"><svg width="20" height="14" viewBox="0 0 20 14"><rect x="2" y="3" width="16" height="8" rx="4" transform="rotate(20 10 7)" fill="none" stroke="#3b8fe0" stroke-width="1.6"/><path d="M10 3v8" stroke="#3b8fe0" stroke-width="1.6" transform="rotate(20 10 7)"/></svg></div><span>DRUGSTORE</span></div>
  <div class="abs dept" style="left:591px;top:570px"><div class="ring"><svg width="18" height="20" viewBox="0 0 18 20"><rect x="1" y="1" width="16" height="18" fill="none" stroke="#3b8fe0" stroke-width="1.4"/><path d="M9 4v12M5 7h8M5 10h8M5 13h8" stroke="#3b8fe0" stroke-width="1.2"/></svg></div><span>X - RAY</span></div>
  <div class="abs dept" style="left:677px;top:570px"><div class="ring"><svg width="18" height="18" viewBox="0 0 18 18"><circle cx="9" cy="9" r="7.5" fill="none" stroke="#3b8fe0" stroke-width="1.6"/><circle cx="9" cy="9" r="3" fill="#3b8fe0"/></svg></div><span>BIRTHS</span></div>
  <div class="abs dept" style="left:763px;top:570px"><div class="ring"><svg width="20" height="20" viewBox="0 0 20 20"><path d="M4 2v6a4 4 0 0 0 8 0V2M8 12v3a3 3 0 0 0 6 0v-4" fill="none" stroke="#3b8fe0" stroke-width="1.6"/><circle cx="14" cy="9" r="2" fill="none" stroke="#3b8fe0" stroke-width="1.4"/></svg></div><span>GENERAL</span></div>
  <div class="abs dept" style="left:849px;top:570px"><div class="ring"><svg width="16" height="18" viewBox="0 0 16 18"><path d="M5 1h6M6 1v6L1 16h14L10 7V1" fill="none" stroke="#3b8fe0" stroke-width="1.6"/><path d="M3 13h10l1 3H2z" fill="#3b8fe0"/></svg></div><span>TESTING</span></div>

  <div class="abs btn-light" style="left:694px;top:649px;width:113px;height:19px">VIEW ALL OUR DEPARTMENTS +</div>

  <!-- doctors -->
  <div class="abs sec-title center" style="left:475px;top:712px;width:551px">Meet our Doctors</div>
  <div class="abs" style="left:740px;top:727px;width:20px;height:1px;background:var(--green)"></div>
  <div class="abs tiny center" style="left:590px;top:738px;width:320px;line-height:6.5px">Lorem ipsum dolor sit amet, consectetur adipiscing elit, sed do eiusmod tempor incididunt ut labore et dolore magna.<br>Ut enim ad minim veniam, quis nostrud exercitation ullamco laboris nisi ut aliquip ex ea commodo</div>
  <div class="abs arrow" style="left:540px;top:795px">&#8592;</div>
  <div class="abs arrow" style="left:942px;top:795px">&#8594;</div>

  <div class="abs doc" style="left:583px;top:766px"><div class="photo" role="img" aria-label="Portrait of Dr. Mark Ellison"></div><h5 style="color:var(--red)">DR. MARK ELLISON</h5><p>Gynecologist</p></div>
  <div class="abs doc" style="left:669px;top:766px"><div class="photo" role="img" aria-label="Portrait of Dr. Sara Lindqvist"></div><div class="social"><i></i><i></i><i></i><i></i></div><h5>DR. SARA LINDQVIST</h5><p>Cardiologist</p></div>
  <div class="abs doc" style="left:755px;top:766px"><div class="photo" role="img" aria-label="Portrait of Dr. Kristin Moyo"></div><h5>DR. KRISTIN MOYO</h5><p>Gynecologist</p></div>
  <div class="abs doc" style="left:841px;top:766px"><div class="photo" role="img" aria-label="Portrait of Dr. Renée Falk"></div><h5>DR. RENÉE FALK</h5><p>Surgeon heart</p></div>

  <!-- testimonial -->
  <div class="abs testi"></div>
  <div class="abs sec-title-w center" style="left:475px;top:900px;width:551px">What our patients are saying</div>
  <div class="abs" style="left:740px;top:915px;width:20px;height:1px;background:#bdeee4"></div>
  <div class="abs avatar" role="img" aria-label="Photo of patient Helena Marsh"></div>
  <div class="abs center" style="left:475px;top:992px;width:551px;font:700 4px 'Montserrat',sans-serif;color:var(--white)">HELENA MARSH</div>
  <div class="abs quote">Nemo enim ipsam voluptatem quia voluptas sit aspernatur aut odit aut fugit, sed quia consequuntur magni dolores eos qui ratione voluptatem sequi nesciunt. Neque porro quisquam est, qui dolorem ipsum quia dolor sit amet, consectetur, adipisci velit, sed quia non numquam eius modi tempora incidunt ut labore</div>
  <div class="abs" style="left:903px;top:992px;font:700 24px/24px 'Montserrat',sans-serif;color:var(--white)">&#8221;</div>
  <div class="abs arrow" style="left:540px;top:961px;background:rgba(255,255,255,.3);color:var(--white)">&#8592;</div>
  <div class="abs arrow" style="left:942px;top:961px;background:rgba(255,255,255,.3);color:var(--white)">&#8594;</div>

  <!-- news -->
  <div class="abs sec-title center" style="left:475px;top:1073px;width:551px">Lastest news</div>
  <div class="abs" style="left:740px;top:1088px;width:20px;height:1px;background:var(--green)"></div>

  <div class="abs news" style="left:583px;top:1102px"><div class="thumb" role="img" aria-label="News photo"></div><div class="date">12<br>MAR</div><div class="body"><h6>Sed ut perspiciatis unde omnis iste quia error sit</h6><p>Voluptatem accusantium doloremque laudantium totam rem aperiam eaque ipsa quae ab illo inventore veritatis et quasi architecto beatae vitae dicta sunt.</p><div class="meta"><span><em>&#9679;</em> NIA PARDO</span><span><em>&#9829;</em> 1432 &nbsp;<em>&#9993;</em> 09</span></div></div></div>
  <div class="abs news" style="left:755px;top:1102px"><div class="thumb" role="img" aria-label="News photo"></div><div class="date">10<br>MAR</div><div class="body"><h6>Dolore perspiciatis unde omnis iste</h6><p>Voluptatem accusantium doloremque laudantium totam rem aperiam eaque ipsa quae ab illo inventore veritatis et quasi architecto beatae vitae dicta sunt.</p><div class="meta"><span><em>&#9679;</em> NIA PARDO</span><span><em>&#9829;</em> 1432 &nbsp;<em>&#9993;</em> 09</span></div></div></div>
  <div class="abs news" style="left:583px;top:1170px"><div class="thumb" role="img" aria-label="News photo"></div><div class="date">7<br>MAR</div><div class="body"><h6>Dolore perspiciatis unde omnis iste</h6><p>Voluptatem accusantium doloremque laudantium totam rem aperiam eaque ipsa quae ab illo inventore veritatis et quasi architecto beatae vitae dicta sunt.</p><div class="meta"><span><em>&#9679;</em> NIA PARDO</span><span><em>&#9829;</em> 1432 &nbsp;<em>&#9993;</em> 09</span></div></div></div>
  <div class="abs news" style="left:755px;top:1170px"><div class="thumb" role="img" aria-label="News photo"></div><div class="date">5<br>MAR</div><div class="body"><h6>Sed ut perspiciatis unde omnis iste quia error sit</h6><p>Voluptatem accusantium doloremque laudantium totam rem aperiam eaque ipsa quae ab illo inventore veritatis et quasi architecto beatae vitae dicta sunt.</p><div class="meta"><span><em>&#9679;</em> NIA PARDO</span><span><em>&#9829;</em> 1432 &nbsp;<em>&#9993;</em> 09</span></div></div></div>

  <!-- stats -->
  <div class="abs stats"></div>
  <div class="abs map" role="img" aria-label="Faint world map backdrop"></div>
  <div class="abs stat" style="left:576px;top:1262px"><b>702</b><span>Our Machines</span><i></i><p>Quis autem vel eum iure reprehenderit qui in ea<br>voluptate velit esse quam nihil</p></div>
  <div class="abs stat" style="left:689px;top:1262px"><b>127</b><span>Our Rooms</span><i></i><p>Quis autem vel eum iure reprehenderit qui in ea<br>voluptate velit esse quam nihil</p></div>
  <div class="abs stat" style="left:805px;top:1262px"><b>364</b><span>Our Staffs</span><i></i><p>Quis autem vel eum iure reprehenderit qui in ea<br>voluptate velit esse quam nihil</p></div>

  <!-- footer -->
  <div class="abs footer"></div>
  <div class="abs cta" style="top:1330px;height:37px">
    <div class="abs" style="left:13px;top:7px;font-size:8px">Confirm avaliability of any Prescription via Mobile</div>
    <div class="abs" style="left:13px;top:19px;width:215px;font-size:3.2px;line-height:4.6px;color:#e6fbf4">Morbi tempor pretium ante, nec semper libero blandit quis. Nulla facilisi. Sed viverra nunc sit amet dapibus commodo. Nam in aliquet ligula, vel feugiat sapien. Suspendisse in mi ornare.</div>
    <div class="abs btn-light" style="left:241px;top:9px;width:80px;height:19px">LEARN MORE</div>
  </div>

  <div class="abs fcol" style="left:583px;top:1387px;width:105px"><h6>CAREWELL HUB</h6><p>Neque porro quisquam est, qui dolorem ipsum quia dolor sit amet, consectetur, adipisci velit, sed quia non numquam eius modi tempora incidunt ut labore et dolore magnam aliquam quaerat voluptatem.</p><p>&#9679; Plot 12, Acacia Avenue, Kololo, Kampala<br>&#9679; +1 800 555 0123<br>&#9679; hello@carewellhub.example<br>&#9679; www.carewellhub.example</p></div>
  <div class="abs fcol" style="left:697px;top:1386px"><h6>&#9679; RECENT TWITTER</h6><p>@carewellnews: Eat quo dolorem ipsum quia dolor sit amet consectetur adipisci velit sed quia<br>2 hours ago</p><p>@clinicdesk: Eat quo dolorem ipsum quia dolor sit amet consectetur adipisci velit sed quia non<br>2 hours ago</p><p>@clinicdesk: Eat quo dolorem ipsum quia dolor sit amet consectetur adipisci velit sed quia non<br>2 hours ago</p></div>
  <div class="abs fcol" style="left:812px;top:1386px"><h6>NEWS LETTER</h6><p>Enter your email and we'll send you a coupon with 10% off your next visit. Add any text here.</p></div>
  <div class="abs" style="left:812px;top:1417px;width:106px;height:13px;border-radius:7px;background:#3b86cc"></div>
  <div class="abs" style="left:890px;top:1417px;width:28px;height:13px;border-radius:7px;background:#a8d3f3;font:700 3.8px/13px 'Montserrat',sans-serif;color:var(--ink);text-align:center">SEND</div>
  <div class="abs social-row" style="left:812px;top:1439px"><i style="background:var(--white)"></i><i></i><i></i><i></i><i></i></div>

  <div class="abs copy">© 2016 Carewell Hub. All Rights Reserved</div>
</div>
</body>
</html>
```